Bref créative
Corvale Power Associates, LLC
Stationery and business cards
Professional
Dean Halvorsen
President
28715 Birchwood Crest Lane
Suite 615
Houston, TX 77084
dean.halvorsen@corvale-pa.com
We will need multiple name, cell phone, and email changes. Primary colors should be white, black, and a vibrant blue.
Here is our logo Ai.

```html
<!DOCTYPE html>
<html lang="en">
<head>
<meta charset="utf-8">
<title>Corvale Power Associates — Stationery</title>
<link rel="stylesheet" href="https://fonts.googleapis.com/css2?family=Arimo:wght@400;700&display=swap">
<style>
  :root {
    --blue: #1a74d1;
    --blue-deep: #0b4f9e;
    --blue-light: #4aa3f0;
    --black: #0c0c0c;
    --white: #ffffff;
    --ink: #333a44;
    --muted: #6b7480;
    --backdrop: #e6e9ed;
  }
  * { box-sizing: border-box; margin: 0; padding: 0; }
  html, body { width: 1200px; height: 871px; overflow: hidden; }
  body {
    background: var(--backdrop);
    font-family: "Arimo", Arial, sans-serif;
    color: var(--ink);
    position: relative;
  }
  .sheet {
    position: absolute;
    background: var(--white);
    box-shadow: 0 2px 8px rgba(0,0,0,.15);
    overflow: hidden;
  }
  .edge-swoosh { position: absolute; left: 0; top: 0; height: 100%; }

  .brand { display: flex; align-items: center; gap: 8px; }
  .brand-dot { border-radius: 50%; background: var(--blue); flex: none; }
  .brand-name { font-weight: 700; color: var(--blue); letter-spacing: .5px; white-space: nowrap; }

  /* Letterhead */
  .letterhead { left: 50px; top: 50px; width: 420px; height: 543px; }
  .letterhead .brand { position: absolute; left: 62px; top: 40px; }
  .letterhead .brand-dot { width: 30px; height: 30px; }
  .letterhead .brand-name { font-size: 17px; }
  .letterhead-footer {
    position: absolute; left: 62px; bottom: 26px;
    font-size: 8px; line-height: 1.55; color: var(--ink);
  }

  /* Envelope front */
  .envelope-front { left: 510px; top: 50px; width: 640px; height: 278px; }
  .envelope-front .brand { position: absolute; left: 56px; top: 28px; }
  .envelope-front .brand-dot { width: 24px; height: 24px; }
  .envelope-front .brand-name { font-size: 14px; }
  .return-address { position: absolute; left: 88px; top: 60px; font-size: 7.5px; color: var(--ink); }

  /* Envelope back */
  .envelope-back { left: 510px; top: 348px; width: 640px; height: 278px; }
  .envelope-back .flap { position: absolute; inset: 0; width: 100%; height: 100%; }
  .envelope-back .brand { position: absolute; left: 50%; top: 132px; transform: translateX(-50%); }
  .envelope-back .brand-dot { width: 22px; height: 22px; background: var(--white); }
  .envelope-back .brand-name { font-size: 13px; color: var(--white); }

  /* Business cards */
  .card { top: 660px; width: 260px; height: 149px; border-radius: 6px; }
  .card-front { left: 50px; }
  .card-front .brand { position: absolute; left: 30px; top: 16px; gap: 5px; }
  .card-front .brand-dot { width: 14px; height: 14px; }
  .card-front .brand-name { font-size: 9.5px; }
  .card-person { position: absolute; left: 30px; top: 86px; }
  .card-person .person-name { font-size: 11px; font-weight: 700; color: var(--black); }
  .card-person .person-title { font-size: 7px; color: var(--muted); margin-top: 2px; }
  .card-details { position: absolute; left: 140px; top: 40px; font-size: 5.5px; line-height: 1.6; color: var(--ink); }

  .card-mark { display: flex; flex-direction: column; align-items: center; justify-content: center; gap: 8px; }
  .card-mark .brand { flex-direction: column; gap: 8px; }
  .card-mark .brand-dot { width: 36px; height: 36px; }
  .card-mark .brand-name { font-size: 15px; }
  .card-web { position: absolute; bottom: 10px; left: 0; right: 0; text-align: center; font-size: 5.5px; }

  .card-blue { left: 330px; background: radial-gradient(ellipse at 40% 35%, var(--blue-light), var(--blue) 55%, var(--blue-deep)); }
  .card-blue .brand-dot { background: var(--white); }
  .card-blue .brand-name { color: var(--white); }
  .card-blue .card-web { color: rgba(255,255,255,.85); }

  .card-black { left: 610px; background: var(--black); }
  .card-black .card-web { color: #9aa3ad; }

  .card-white { left: 890px; }
  .card-white .card-web { color: var(--muted); }
</style>
</head>
<body>

  <section class="sheet letterhead">
    <svg class="edge-swoosh" width="60" height="543" viewBox="0 0 60 543" preserveAspectRatio="none">
      <defs>
        <linearGradient id="lh-blue" x1="0" y1="0" x2="0" y2="1">
          <stop offset="0" stop-color="#0b4f9e"/>
          <stop offset=".5" stop-color="#1a74d1"/>
          <stop offset="1" stop-color="#4aa3f0"/>
        </linearGradient>
      </defs>
      <path d="M0 0 H26 C14 150 40 330 30 543 H0 Z" fill="url(#lh-blue)"/>
      <path d="M26 0 C14 150 40 330 30 543 H36 C46 330 22 150 33 0 Z" fill="#0c0c0c"/>
    </svg>
    <div class="brand"><span class="brand-dot"></span><span class="brand-name">Corvale Power Associates</span></div>
    <address class="letterhead-footer">
      28715 Birchwood Crest Lane, Suite 615, Houston, TX 77084<br>
      p 281-555-0193 &nbsp;|&nbsp; c 832-555-0147<br>
      e dean.halvorsen@corvale-pa.com &nbsp;|&nbsp; w www.corvalepa.com
    </address>
  </section>

  <section class="sheet envelope-front">
    <svg class="edge-swoosh" width="44" height="278" viewBox="0 0 44 278" preserveAspectRatio="none">
      <defs>
        <linearGradient id="env-blue" x1="0" y1="0" x2="0" y2="1">
          <stop offset="0" stop-color="#0b4f9e"/>
          <stop offset="1" stop-color="#4aa3f0"/>
        </linearGradient>
      </defs>
      <path d="M0 0 H20 C12 90 30 180 22 278 H0 Z" fill="url(#env-blue)"/>
      <path d="M20 0 C12 90 30 180 22 278 H26 C34 180 16 90 25 0 Z" fill="#0c0c0c"/>
    </svg>
    <div class="brand"><span class="brand-dot"></span><span class="brand-name">Corvale Power Associates</span></div>
    <address class="return-address">28715 Birchwood Crest Lane, Suite 615, Houston, TX 77084</address>
  </section>

  <section class="sheet envelope-back">
    <svg class="flap" viewBox="0 0 640 278" preserveAspectRatio="none">
      <defs>
        <linearGradient id="flap-blue" x1="0" y1="0" x2="0" y2="1">
          <stop offset="0" stop-color="#4aa3f0"/>
          <stop offset=".6" stop-color="#1a74d1"/>
          <stop offset="1" stop-color="#0b4f9e"/>
        </linearGradient>
      </defs>
      <path d="M0 278 L300 150 Q320 142 340 150 L640 278" fill="none" stroke="#d7dbe0" stroke-width="1.5"/>
      <path d="M0 0 H640 L345 176 Q320 190 295 176 Z" fill="url(#flap-blue)"/>
    </svg>
    <div class="brand"><span class="brand-dot"></span><span class="brand-name">Corvale</span></div>
  </section>

  <section class="sheet card card-front">
    <svg class="edge-swoosh" width="22" height="149" viewBox="0 0 22 149" preserveAspectRatio="none">
      <path d="M0 0 H12 C6 50 16 100 11 149 H0 Z" fill="#1a74d1"/>
      <path d="M12 0 C6 50 16 100 11 149 H14 C19 100 9 50 15 0 Z" fill="#0c0c0c"/>
    </svg>
    <div class="brand"><span class="brand-dot"></span><span class="brand-name">Corvale Power Associates</span></div>
    <div class="card-person">
      <p class="person-name">Dean Halvorsen</p>
      <p class="person-title">President</p>
    </div>
    <address class="card-details">
      28715 Birchwood Crest Lane<br>
      Suite 615<br>
      Houston, TX 77084<br>
      p 281-555-0193<br>
      c 832-555-0147<br>
      dean.halvorsen@corvale-pa.com
    </address>
  </section>

  <section class="sheet card card-mark card-blue">
    <div class="brand"><span class="brand-dot"></span><span class="brand-name">Corvale</span></div>
    <p class="card-web">www.corvalepa.com</p>
  </section>

  <section class="sheet card card-mark card-black">
    <div class="brand"><span class="brand-dot"></span><span class="brand-name">Corvale</span></div>
    <p class="card-web">www.corvalepa.com</p>
  </section>

  <section class="sheet card card-mark card-white">
    <div class="brand"><span class="brand-dot"></span><span class="brand-name">Corvale</span></div>
    <p class="card-web">www.corvalepa.com</p>
  </section>

</body>
</html>
```